Brackwell Removals

We are a domestic removals company, providing the following service:
- removals service
- packing service
- packing materials
- storage facility
- furniture dismantling and reassembling
We would like to start a flyer campaign to customers that just agreed for the house sale.
Our strong key points:
- Good Reviews (Ratewise, Zenquor, trulyshifting.com and plazabook)
- Two Men Service (we do all the heavy work for the customer, and place the furniture and boxes to each room of destination)
- Fully Insured
- We can take bookings 7-days of week
- Free and no-obligation survey (we need to do a house visit first in order to provide a fixed and accurate quote)
- Free Quote
Technical Specs:
Landline number: 01632 960418
Contact email: office@brackwellremovals.example.co.uk
Address: Unit 14, Corrin Lane, Northampton NN9 4XQ
Website: brackwellremovals.example.co.uk
Took a look on the onto previous projects on PV.com, and liked several flyers already done by you guys, for this industry
We'd like to integrate the colours from our logo in the flyer as well !!

```html
<!DOCTYPE html>
<html lang="en">
<head>
<meta charset="utf-8">
<title>Brackwell Removals – Flyer</title>
<link rel="stylesheet" href="https://fonts.googleapis.com/css2?family=Bebas+Neue&family=Montserrat:wght@700;800;900&family=Open+Sans:wght@400;600;700&display=swap">
<style>
  :root {
    --stage: #6b6b6b;
    --paper: #ffffff;
    --panel: #24262c;
    --panel-deep: #18191d;
    --orange: #f58220;
    --orange-soft: #ef8a3c;
    --teal: #0e8a8a;
    --ink: #333436;
    --red: #c22a0c;
    --red-bright: #d81e1e;
    --yellow: #e9d52c;
    --white: #ffffff;
    --quote-text: #f3e1e1;
  }
  * { margin: 0; padding: 0; box-sizing: border-box; }
  html, body { width: 1200px; height: 906px; overflow: hidden; background: var(--stage); }
  .flyer {
    position: absolute; left: 66px; top: 54px; width: 1068px; height: 781px;
    background: var(--panel); overflow: hidden;
    font-family: "Open Sans", sans-serif;
  }
  .brand-area { position: absolute; left: 0; top: 0; width: 499px; height: 172px; background: var(--paper); }
  .brand-mark { position: absolute; left: 86px; top: 26px; width: 120px; height: 120px; border-radius: 50%; background: var(--ink); }
  .brand-name {
    position: absolute; left: 222px; top: 48px; width: 260px;
    font-family: "Montserrat", sans-serif; font-weight: 900; font-size: 31px; line-height: 36px;
    color: var(--teal); text-transform: uppercase;
  }
  .hero-photo {
    position: absolute; left: 0; top: 172px; width: 499px; height: 489px;
    background: linear-gradient(160deg, #8fb4de 0%, #c9d9ea 35%, #2f49a8 70%, #1c2c6e 100%);
  }
  .info-panel { position: absolute; left: 499px; top: 0; width: 569px; height: 661px;
    background: radial-gradient(circle at 60% 40%, #2d3036 0%, var(--panel) 60%, var(--panel-deep) 100%); }
  .headline { position: absolute; left: 0; width: 100%; text-align: center; font-family: "Bebas Neue", sans-serif; color: var(--orange); }
  .headline--top { top: 28px; font-size: 72px; line-height: 64px; left: 4px; }
  .headline--main { top: 96px; font-size: 68px; line-height: 60px; left: 4px; }
  .subheadline { position: absolute; top: 172px; left: 0; width: 100%; text-align: center;
    font-family: "Bebas Neue", sans-serif; font-size: 35px; line-height: 32px; color: var(--white); left: 4px; }
  .key-points { position: absolute; left: 43px; top: 230px; width: 270px; list-style: none; }
  .key-points li { position: relative; padding-left: 21px; font-size: 13px; line-height: 17.3px; color: #e9e9ea; margin-bottom: 7px; }
  .key-points svg { position: absolute; left: 0; top: 2px; width: 14px; height: 14px; }
  .divider { position: absolute; left: 327px; top: 238px; width: 1px; height: 170px; background: #8b6a2c; }
  .services { position: absolute; left: 355px; top: 229px; list-style: none; }
  .services li { position: relative; padding-left: 31px; height: 29.7px; font-weight: 700; font-size: 16px; line-height: 20px; color: var(--white); }
  .services svg { position: absolute; left: 0; top: 2px; width: 17px; height: 16px; }
  .quote-button {
    position: absolute; left: 56px; top: 426px; width: 479px; height: 92px; border-radius: 14px;
    background: linear-gradient(180deg, var(--red-bright) 0%, #c81a1a 44%, var(--orange-soft) 44%, #e8742c 100%);
    border: 2px solid #f6d4c2; text-align: center;
    font-family: "Montserrat", sans-serif; font-weight: 900; font-size: 66px; line-height: 88px; color: var(--quote-text);
    letter-spacing: 1px;
  }
  .booking-line { position: absolute; left: 0; width: 100%; text-align: center; font-family: "Montserrat", sans-serif; }
  .booking-line--big { top: 540px; font-size: 58px; font-weight: 800; line-height: 66px; color: var(--white); left: 4px; }
  .booking-line--small { top: 606px; font-size: 27px; font-weight: 700; line-height: 34px; color: var(--yellow); left: 2px; }
  .footer { position: absolute; left: 0; top: 661px; width: 1068px; height: 120px; background: var(--red); }
  .footer-call { position: absolute; left: 0; top: 0; width: 100%; height: 100%; }
  .contact-label { position: absolute; left: 41px; top: 13px; font-family: "Montserrat", sans-serif; font-weight: 800; font-size: 18px; color: var(--yellow); }
  .phone-icon { position: absolute; left: 40px; top: 53px; width: 28px; height: 28px; }
  .phone-number { position: absolute; left: 83px; top: 38px; font-family: "Bebas Neue", sans-serif; font-size: 54px; line-height: 56px; color: var(--white); letter-spacing: 1px; }
  .pin-icon { position: absolute; left: 399px; top: 45px; width: 24px; height: 28px; }
  .address { position: absolute; left: 456px; top: 33px; font-family: "Montserrat", sans-serif; font-weight: 700; font-size: 18px; line-height: 25px; color: var(--white); }
  .web-icon, .mail-icon { position: absolute; left: 714px; width: 25px; height: 25px; }
  .web-icon { top: 27px; } .mail-icon { top: 62px; }
  .web-link, .mail-link { position: absolute; left: 756px; font-family: "Montserrat", sans-serif; font-weight: 700; color: var(--white); }
  .web-link { top: 30px; font-size: 13.5px; letter-spacing: 0.6px; }
  .mail-link { top: 64px; font-size: 14px; }
</style>
</head>
<body>
<main class="flyer">
  <header class="brand-area">
    <div class="brand-mark"></div>
    <div class="brand-name">Brackwell Removals</div>
  </header>

  <div class="hero-photo" role="img" aria-label="Photo of two movers in blue overalls carrying branded cardboard boxes from a van, blue sky and brick building behind"></div>

  <section class="info-panel">
    <h1 class="headline headline--top">We are</h1>
    <h1 class="headline headline--main">A Domestic Removals</h1>
    <h2 class="subheadline">Company, providing the following service</h2>

    <ul class="key-points">
      <li><svg viewBox="0 0 14 14"><circle cx="7" cy="7" r="6" fill="none" stroke="#f58220" stroke-width="1.6"/><path d="M4 7l2.2 2.2L12 3" fill="none" stroke="#f58220" stroke-width="1.8"/></svg>Good Reviews (Ratewise, Zenquor, trulyshifting.com, and plazabook)</li>
      <li><svg viewBox="0 0 14 14"><circle cx="7" cy="7" r="6" fill="none" stroke="#f58220" stroke-width="1.6"/><path d="M4 7l2.2 2.2L12 3" fill="none" stroke="#f58220" stroke-width="1.8"/></svg>Two Men Service (we do all the heavy work for the customer, and place the furniture and boxes to each room of destination)</li>
      <li><svg viewBox="0 0 14 14"><circle cx="7" cy="7" r="6" fill="none" stroke="#f58220" stroke-width="1.6"/><path d="M4 7l2.2 2.2L12 3" fill="none" stroke="#f58220" stroke-width="1.8"/></svg>Fully Insured</li>
      <li><svg viewBox="0 0 14 14"><circle cx="7" cy="7" r="6" fill="none" stroke="#f58220" stroke-width="1.6"/><path d="M4 7l2.2 2.2L12 3" fill="none" stroke="#f58220" stroke-width="1.8"/></svg>Free and no-obligation survey (we need to do a house visit first in order to provide a fixed and accurate quote)</li>
    </ul>

    <div class="divider"></div>

    <ul class="services">
      <li><svg viewBox="0 0 17 16"><rect x="1" y="4" width="9" height="8" fill="#f58220"/><path d="M10 7h4l2 3v2h-6z" fill="#f58220"/><circle cx="4" cy="13" r="2" fill="#f58220"/><circle cx="13" cy="13" r="2" fill="#f58220"/></svg>Removals Service</li>
      <li><svg viewBox="0 0 17 16"><path d="M2 7l6.5 3L15 7v6l-6.5 3L2 13z" fill="#f58220"/><path d="M8.5 1v5M6 3.5l2.5 2.5L11 3.5" stroke="#f58220" stroke-width="1.6" fill="none"/></svg>Packing Service</li>
      <li><svg viewBox="0 0 17 16"><rect x="1" y="3" width="10" height="9" fill="#f58220"/><path d="M11 6h3l2 3v3h-5z" fill="#f58220"/><circle cx="5" cy="14" r="1.8" fill="#f58220"/></svg>Packing Materials</li>
      <li><svg viewBox="0 0 17 16"><path d="M1 6l7.5-5L16 6v9H1z" fill="#f58220"/><rect x="4" y="8" width="9" height="5" fill="#24262c"/></svg>Storage Facility</li>
      <li><svg viewBox="0 0 17 16"><path d="M3 6a5.5 4 0 0 1 11 0v3H3z" fill="#f58220"/><rect x="1" y="8" width="15" height="5" rx="2" fill="#f58220"/></svg>Furniture Dismantling</li>
      <li><svg viewBox="0 0 17 16"><circle cx="5" cy="3" r="2" fill="#f58220"/><path d="M3 6h4v5H3zM3 11l-1 4M7 11l1 4" stroke="#f58220" stroke-width="1.6" fill="#f58220"/><rect x="10" y="6" width="6" height="8" fill="none" stroke="#f58220" stroke-width="1.5"/></svg>Reassembling</li>
    </ul>

    <div class="quote-button">FREE QUOTE</div>

    <p class="booking-line booking-line--big">WE CAN TAKE</p>
    <p class="booking-line booking-line--small">BOOKINGS 7-DAYS OF WEEK</p>
  </section>

  <footer class="footer">
    <svg class="footer-call" viewBox="0 0 1068 120" preserveAspectRatio="none"><path d="M0 0H336L380 120H0z" fill="#18191d"/></svg>
    <p class="contact-label">CONTACT US TODAY!</p>
    <svg class="phone-icon" viewBox="0 0 28 28"><circle cx="14" cy="14" r="13" fill="#fff"/><path d="M10 7c-2 1-3 3-2 7s4 7 7 7c1 0 2-1 2-2l-2-2-2 1c-2-1-3-3-3-5l1-1-1-5z" fill="#18191d"/></svg>
    <p class="phone-number">01632 960418</p>
    <svg class="pin-icon" viewBox="0 0 24 28"><path d="M12 1a10 10 0 0 0-10 10c0 7 10 16 10 16s10-9 10-16A10 10 0 0 0 12 1z" fill="#fff"/><circle cx="12" cy="11" r="4" fill="#c22a0c"/></svg>
    <p class="address">Unit 14, Corrin Lane,<br>Northampton NN9 4XQ</p>
    <svg class="web-icon" viewBox="0 0 25 25"><circle cx="12.5" cy="12.5" r="11" fill="none" stroke="#fff" stroke-width="2"/><ellipse cx="12.5" cy="12.5" rx="5" ry="11" fill="none" stroke="#fff" stroke-width="1.6"/><path d="M1.5 12.5h22M3.5 7h18M3.5 18h18" stroke="#fff" stroke-width="1.4"/></svg>
    <p class="web-link">www.brackwellremovals.example.co.uk</p>
    <svg class="mail-icon" viewBox="0 0 25 25"><circle cx="12.5" cy="12.5" r="12" fill="#fff"/><rect x="6" y="8" width="13" height="9" fill="none" stroke="#c22a0c" stroke-width="1.5"/><path d="M6 8l6.5 5L19 8M6 17l5-4M19 17l-5-4" fill="none" stroke="#c22a0c" stroke-width="1.3"/></svg>
    <p class="mail-link">office@brackwellremovals.example.co.uk</p>
  </footer>
</main>
</body>
</html>
```